New Webpage for High Class Expert Witness Services Company

We are looking for a minimalist design for a webpage that just has our logo and an entry form offer to connect with one of our Liaisons.
The entry form should just ask for Name, Email, Contact Info and Description of Project.

Company Name is: The Marlow Crest Advisory Services

Number of Pages Required

1 page

```html
<!DOCTYPE html>
<html lang="en">
<head>
<meta charset="utf-8">
<title>The Marlow Crest Advisory Services — Connect With a Liaison</title>
<link rel="stylesheet" href="https://fonts.googleapis.com/css2?family=Cinzel:wght@400;700&family=Inter:wght@300;500&display=swap">
<style>
  :root {
    --ink: #ffffff;
    --muted: #b9b0aa;
    --placeholder: #c9c2bd;
    --brand: #e7e3e1;
    --panel-top: #221611;
    --panel-mid: #2b1c15;
    --panel-glow: #54382a;
    --panel-edge: #140d0a;
    --field: rgba(255, 255, 255, 0.055);
    --shelf-a: #3a1a16;
    --shelf-b: #6b3a28;
    --shelf-c: #1b1a1f;
    --button-text: #1d1410;
  }
  * { box-sizing: border-box; margin: 0; padding: 0; }
  html, body { width: 1200px; height: 818px; overflow: hidden; }
  body {
    position: relative;
    font-family: "Inter", sans-serif;
    color: var(--ink);
    background: var(--shelf-c);
  }
  .backdrop {
    position: absolute; inset: 0;
    background: linear-gradient(90deg, var(--shelf-a) 0%, var(--shelf-b) 12%, var(--shelf-a) 30%, #4a2419 55%, var(--shelf-a) 78%, #2a2a22 100%);
  }
  .panel {
    position: absolute;
    left: 31px; top: 29px; width: 1139px; height: 760px;
    background:
      radial-gradient(ellipse 520px 300px at 25% 100%, var(--panel-glow) 0%, rgba(84,56,42,0) 100%),
      radial-gradient(ellipse 600px 400px at 50% 25%, var(--panel-mid) 0%, rgba(43,28,21,0) 100%),
      linear-gradient(135deg, var(--panel-top) 0%, var(--panel-mid) 55%, var(--panel-edge) 100%);
  }
  .brand {
    position: absolute; left: 0; right: 0; top: 37px;
    display: flex; justify-content: center; align-items: center; gap: 14px;
  }
  .brand-mark { width: 32px; height: 32px; border: 2px solid var(--brand); }
  .brand-name {
    font-family: "Cinzel", serif; font-weight: 400;
    font-size: 20px; line-height: 23px; letter-spacing: 1px;
    color: var(--brand); text-transform: uppercase;
  }
  .heading {
    position: absolute; left: 0; right: 0; top: 194px;
    font-family: "Cinzel", serif; text-align: center; line-height: 39px;
  }
  .heading-light { display: block; font-size: 37px; font-weight: 400; }
  .heading-bold { display: block; font-size: 37px; font-weight: 700; }
  .contact-form { position: absolute; left: 107px; top: 311px; width: 924px; }
  .row { display: flex; gap: 8px; margin-bottom: 14px; }
  .field {
    position: relative; flex: 1; height: 47px;
    background: var(--field); border-radius: 2px;
    display: flex; align-items: center; padding: 0 33px;
    font-size: 13px; font-weight: 300; color: var(--placeholder);
  }
  .field svg { position: absolute; right: 21px; top: 50%; transform: translateY(-50%); }
  .field.area { height: 131px; align-items: flex-start; padding-top: 22px; margin-top: -6px; }
  .field.area svg { top: 29px; }
  .form-foot { display: flex; justify-content: space-between; align-items: flex-start; margin-top: 24px; }
  .consent {
    display: flex; align-items: center; gap: 6px; margin-top: -6px;
    font-size: 11.5px; font-weight: 300; color: var(--muted); height: 14px;
  }
  .submit {
    width: 141px; height: 42px; background: var(--ink); border: 0; border-radius: 2px;
    font-family: "Inter", sans-serif; font-weight: 500; font-size: 14px; color: var(--button-text);
  }
</style>
</head>
<body>
  <div class="backdrop" role="img" aria-label="Shelf of antique leather-bound books"></div>
  <main class="panel">
    <header class="brand">
      <span class="brand-mark"></span>
      <div class="brand-name">The Marlow Crest<br>Advisory Services</div>
    </header>

    <h1 class="heading">
      <span class="heading-light">CONNECT WITH ONE OF</span>
      <span class="heading-bold">OUR LIAISONS</span>
    </h1>

    <form class="contact-form">
      <div class="row">
        <div class="field">First Name..
          <svg width="14" height="16" viewBox="0 0 14 16" fill="#fff"><circle cx="7" cy="4" r="4"/><path d="M0 16c0-5 3-7 7-7s7 2 7 7z"/></svg>
        </div>
        <div class="field">Last Name..
          <svg width="14" height="16" viewBox="0 0 14 16" fill="#fff"><circle cx="7" cy="4" r="4"/><path d="M0 16c0-5 3-7 7-7s7 2 7 7z"/></svg>
        </div>
      </div>
      <div class="row">
        <div class="field">Phone no..
          <svg width="15" height="15" viewBox="0 0 16 16" fill="#fff"><path d="M15.5 12.2l-3.3-1.6c-.5-.2-1-.1-1.3.3l-1.2 1.4C7.4 11.3 5 9 3.9 6.6L5.3 5.4c.4-.3.5-.8.3-1.3L4 .8C3.8.2 3.2 0 2.7.2L.6 1C.2 1.2 0 1.6 0 2c.3 7.7 6.3 13.7 14 14 .4 0 .8-.2 1-.6l.7-2.1c.2-.5 0-1-.2-1.1z"/></svg>
        </div>
        <div class="field">Email Add..
          <svg width="16" height="12" viewBox="0 0 16 12" fill="#fff"><path d="M0 1.5V1a1 1 0 0 1 1-1h14a1 1 0 0 1 1 1v.5L8 7z"/><path d="M0 3.3V11a1 1 0 0 0 1 1h14a1 1 0 0 0 1-1V3.3L8 9z"/></svg>
        </div>
      </div>
      <div class="row">
        <div class="field area">Description of Project...
          <svg width="16" height="15" viewBox="0 0 16 15" fill="#fff"><path d="M2 0h12a2 2 0 0 1 2 2v8a2 2 0 0 1-2 2H9l-3 3v-3H2a2 2 0 0 1-2-2V2a2 2 0 0 1 2-2z"/><circle cx="4.5" cy="6" r="1.1" fill="#2b1c15"/><circle cx="8" cy="6" r="1.1" fill="#2b1c15"/><circle cx="11.5" cy="6" r="1.1" fill="#2b1c15"/></svg>
        </div>
      </div>
      <div class="form-foot">
        <label class="consent">
          <svg width="13" height="13" viewBox="0 0 14 14" fill="none" stroke="#b9b0aa" stroke-width="1"><circle cx="7" cy="7" r="6.3"/><path d="M4 7.2l2 2 4-4"/></svg>
          i accept the privacy policy and terms of use
        </label>
        <button class="submit" type="button">Submit Now</button>
      </div>
    </form>
  </main>
</body>
</html>
```